Lone Prairie Canvas & Sound Jubilee

Organization:
Lone Prairie Canvas and Sound Jubilee is a non-profit organization created by a group of anonymous donors to bring more fun, culture, and art to a small Texas town. Our mission is to promote art and music in Washington County.
The multi-day eclectic festival will feature three stages, a film, art vendors, live mural artists, and food trucks set up throughout historic downtown Brenham. The event is FREE to the public.
Goals:
We need an attractive poster to publicize the festival.
Details:
Lone Prairie Canvas and Sound Jubilee
Friday, October 14 – 16
Free admission (VIP tickets available)
Live music- 3 stages/10 bands
Film Screening
Art vendors and art walk
Live art murals
Food trucks
www.loneprairiecanvasandsoundjubilee.example
#loneprairiecanvasandsound
Requirements:
Please incorporate our festival logo attached.
Conclusion:
After selecting a poster design, we hope to continue to work with the artist to design other event materials including website splash page and rack cards using design elements from the poster.

```html
<!DOCTYPE html>
<html lang="en">
<head>
<meta charset="utf-8">
<title>Lone Prairie Canvas and Sound Jubilee</title>
<link href="https://fonts.googleapis.com/css2?family=Saira+Condensed:wght@500;600&family=Archivo+Black&family=Rubik+Dirt&family=Oswald:wght@400;500&family=Roboto+Condensed:ital,wght@1,500&family=Anton&display=swap" rel="stylesheet">
<style>
  :root {
    --red: #e0161c;
    --red-band: #d41219;
    --black: #0d0d0d;
    --white: #ffffff;
    --grey-light: #e3e3e3;
    --grey-mid: #a9a9a9;
    --text-dark: #1a1a1a;
  }
  * { margin: 0; padding: 0; box-sizing: border-box; }
  html, body { width: 869px; height: 1200px; overflow: hidden; background: var(--white); }
  .poster { position: relative; width: 869px; height: 1200px; overflow: hidden; background: var(--white); }
  .poster-art { position: absolute; inset: 0; width: 869px; height: 1200px; }

  .title-top {
    position: absolute; left: 0; width: 869px; top: 510px;
    text-align: center; color: var(--red);
    font-family: "Saira Condensed", sans-serif; font-weight: 600;
    font-size: 88px; line-height: 1; letter-spacing: 1px;
    text-shadow: 3px 3px 0 rgba(0,0,0,0.18);
  }
  .title-bottom {
    position: absolute; left: 0; width: 869px; top: 648px;
    text-align: center; color: var(--black);
    font-family: "Archivo Black", sans-serif;
    font-size: 92px; line-height: 1; letter-spacing: -1px;
  }
  .date-band {
    position: absolute; left: 0; top: 783px; width: 869px; height: 112px;
    background: var(--red-band);
    display: flex; align-items: center; padding-left: 62px; gap: 44px;
    color: var(--white);
  }
  .date-day { font-family: "Rubik Dirt", sans-serif; font-size: 62px; letter-spacing: 2px; }
  .date-year { font-family: "Archivo Black", sans-serif; font-size: 82px; letter-spacing: 1px; }

  .details { position: absolute; left: 66px; top: 920px; color: var(--text-dark); }
  .details-heading {
    font-family: "Anton", sans-serif; font-size: 21px; letter-spacing: 1.5px; margin-bottom: 10px;
  }
  .feature-list {
    list-style: none; display: grid; grid-template-columns: 274px 180px; row-gap: 3px;
    font-family: "Roboto Condensed", sans-serif; font-style: italic; font-weight: 500; font-size: 15.5px;
  }
  .feature-list li { position: relative; padding-left: 13px; }
  .feature-list li::before {
    content: ""; position: absolute; left: 0; top: 7px; width: 6px; height: 6px;
    border-radius: 50%; background: var(--red);
  }

  .festival-mark {
    position: absolute; left: 572px; top: 966px; width: 270px;
    display: flex; align-items: center; gap: 12px;
  }
  .festival-mark-dot { flex: none; width: 46px; height: 46px; border-radius: 50%; background: var(--black); }
  .festival-mark-name {
    font-family: "Oswald", sans-serif; font-weight: 500; font-size: 24px; line-height: 1.1;
    color: var(--black);
  }

  .hashtag {
    position: absolute; left: 56px; top: 1093px; color: var(--white);
    font-family: "Oswald", sans-serif; font-weight: 400; font-size: 30px; letter-spacing: 0.5px;
    text-transform: uppercase;
  }
  .website {
    position: absolute; left: 58px; top: 1144px; color: var(--red);
    font-family: "Oswald", sans-serif; font-weight: 400; font-size: 20px;
    text-transform: uppercase;
  }
</style>
</head>
<body>
<main class="poster">
  <svg class="poster-art" viewBox="0 0 869 1200" aria-hidden="false">
    <defs>
      <linearGradient id="stageFade" x1="0" y1="0" x2="0" y2="1">
        <stop offset="0" stop-color="#4a4a4a"/>
        <stop offset="0.45" stop-color="#9a9a9a"/>
        <stop offset="0.8" stop-color="#dcdcdc"/>
        <stop offset="1" stop-color="#ffffff"/>
      </linearGradient>
      <radialGradient id="stageLights" cx="0.55" cy="0.3" r="0.6">
        <stop offset="0" stop-color="#ffffff" stop-opacity="0.55"/>
        <stop offset="1" stop-color="#ffffff" stop-opacity="0"/>
      </radialGradient>
      <radialGradient id="leadPhoto" cx="0.5" cy="0.45" r="0.6">
        <stop offset="0" stop-color="#c2332e"/>
        <stop offset="0.45" stop-color="#3c4f8f"/>
        <stop offset="1" stop-color="#1b2448"/>
      </radialGradient>
      <radialGradient id="leftPhoto" cx="0.45" cy="0.45" r="0.6">
        <stop offset="0" stop-color="#d8d2c8"/>
        <stop offset="1" stop-color="#6b6660"/>
      </radialGradient>
      <radialGradient id="rightPhoto" cx="0.5" cy="0.5" r="0.6">
        <stop offset="0" stop-color="#8a8a8a"/>
        <stop offset="1" stop-color="#111111"/>
      </radialGradient>
      <linearGradient id="silverRing" x1="0" y1="0" x2="0" y2="1">
        <stop offset="0" stop-color="#f4f4f4"/>
        <stop offset="1" stop-color="#9c9c9c"/>
      </linearGradient>
    </defs>

    <g class="stage-backdrop" role="img" aria-label="Black and white photo of a concert stage with lighting rigs and crowd">
      <rect x="0" y="0" width="869" height="500" fill="url(#stageFade)"/>
      <rect x="0" y="0" width="869" height="420" fill="url(#stageLights)"/>
    </g>

    <g class="photo-circle photo-left">
      <circle cx="133" cy="343" r="131" fill="var(--red)"/>
      <circle cx="133" cy="343" r="124" fill="url(#silverRing)"/>
      <circle cx="133" cy="343" r="118" fill="url(#leftPhoto)" role="img" aria-label="Sepia photo of a guitarist with long hair"/>
    </g>
    <g class="photo-circle photo-right">
      <circle cx="730" cy="343" r="128" fill="var(--red)"/>
      <circle cx="730" cy="343" r="121" fill="url(#silverRing)"/>
      <circle cx="730" cy="343" r="115" fill="url(#rightPhoto)" role="img" aria-label="Black and white photo of a guitarist playing electric guitar"/>
    </g>
    <g class="photo-circle photo-lead">
      <circle cx="442" cy="262" r="210" fill="var(--red)"/>
      <circle cx="442" cy="262" r="201" fill="url(#silverRing)"/>
      <circle cx="442" cy="262" r="193" fill="url(#leadPhoto)" role="img" aria-label="Colour photo of a singer in a red suit performing with a band"/>
    </g>

    <g class="footer-band">
      <polygon points="0,1050 440,1050 560,1130 869,1130 869,1145 555,1145 435,1060 0,1060" fill="var(--grey-mid)"/>
      <polygon points="0,1064 434,1064 556,1150 869,1150 869,1200 0,1200" fill="var(--black)"/>
    </g>
  </svg>

  <h1 class="title-top">LONE PRAIRIE CANVAS AND</h1>
  <h2 class="title-bottom">SOUND JUBILEE</h2>

  <div class="date-band">
    <span class="date-day">14 TH OCTOBER</span>
    <span class="date-year">2016</span>
  </div>

  <section class="details">
    <h3 class="details-heading">FREE ADMISSION</h3>
    <ul class="feature-list">
      <li>Live music- 3 stages/10 bands</li>
      <li>Live art murals</li>
      <li>Film Screening</li>
      <li>Food trucks</li>
      <li>Art vendors and art walk</li>
    </ul>
  </section>

  <div class="festival-mark">
    <span class="festival-mark-dot"></span>
    <span class="festival-mark-name">Lone Prairie Canvas &amp; Sound Jubilee</span>
  </div>

  <p class="hashtag">#loneprairiecanvasandsound</p>
  <p class="website">www.loneprairiecanvasandsoundjubilee.example</p>
</main>
</body>
</html>
```